Powerpt Design Template for QV7LM

A powerpt design template for QV7lm. A simple layout utilizing my company in the design. www.qv7lm.example . Please use the color pallet from the website and the name, etc. You can use general content from the website but I also need to be able to add slides and utilize the design for multiple purposes.

Target Market(s)

Education

Requirements
Must have
• utlize the design and colors from www.qv7lm.example
Nice to have
• use some general content from the website for "about" qv7lm. More importantly, i need to be able to add slides

```html
<!DOCTYPE html>
<html lang="en">
<head>
<meta charset="utf-8">
<title>QV7lm Presentation Template</title>
<link rel="stylesheet" href="https://fonts.googleapis.com/css2?family=Quicksand:wght@400&display=swap">
<style>
  :root {
    --paper: #ffffff;
    --sun-yellow: #ffda6d;
    --warm-orange: #f59e5d;
    --coral: #f3865e;
    --steel-light: #c9c9c7;
    --steel-white: #fbfbfa;
    --steel-mid: #b2b1b3;
    --steel-dark: #676b63;
    --brand-text: #ffffff;
  }
  html, body {
    margin: 0;
    padding: 0;
    overflow: hidden;
    background: var(--paper);
  }
  .slide {
    position: relative;
    width: 1200px;
    height: 1000px;
    background: var(--paper);
    overflow: hidden;
  }
  .slide-shapes {
    position: absolute;
    inset: 0;
  }
  .brand-band {
    position: absolute;
    left: 640px;
    top: 878px;
    width: 560px;
    height: 122px;
    background: linear-gradient(90deg,
      var(--steel-light) 0%,
      #e9e9e5 10%,
      var(--steel-white) 32%,
      var(--steel-light) 45%,
      var(--steel-mid) 62%,
      #8a8c88 78%,
      var(--steel-dark) 100%);
  }
  .triangle-yellow { fill: var(--sun-yellow); }
  .triangle-orange { fill: var(--warm-orange); }
  .triangle-coral { fill: var(--coral); }
  .brand-name {
    position: absolute;
    left: 956px;
    top: 900px;
    height: 60px;
    line-height: 60px;
    font-family: "Quicksand", sans-serif;
    font-weight: 400;
    font-size: 58px;
    letter-spacing: 2px;
    color: var(--brand-text);
  }
</style>
</head>
<body>
  <div class="slide">
    <div class="brand-band"></div>
    <svg class="slide-shapes" width="1200" height="1000" viewBox="0 0 1200 1000" aria-hidden="true">
      <polygon class="triangle-yellow" points="0,528 375,746 0,960"/>
      <polygon class="triangle-orange" points="50,998 422,784 422,998"/>
      <polygon class="triangle-coral" points="480,784 853,998 482,998"/>
    </svg>
    <div class="brand-name">QV7lm</div>
  </div>
</body>
</html>
```